Creative Web design for Tattoo Artist

I am a tattoo artist with a private tattoo/art studio in Spring, TX. I need to design a website for my studio, to include the following "pages" :
-home/about
-FAQ
-Gallery
-Inquiries
-shop
We would like to see designs that are more dark or "moody", and like the colors black/gold.
I'd like my website to reflect my studio, an award winning private, upscale custom only tattoo studio.

I've attached some examples of styles we liked.

Target Market(s)

adults ages 18-50, interested in tattoos, or fine art

Industry/Entity Type

Tattoos/Fine Art/Arts

Coding

Coded - Design and coding required

Number of Pages Required

5+ page

Colors

Designer to choose colors to be used in the design.

Requirements
Must have
• gallery section, and e-commerce page set up so I can begin selling merchandise, I'd like the fonts to flow with my logo design

```html
<!DOCTYPE html>
<html lang="en">
<head>
<meta charset="utf-8">
<title>The Gilded Viper — Private Tattoo Studio</title>
<link rel="stylesheet" href="https://fonts.googleapis.com/css2?family=Cinzel:wght@500;700&display=swap">
<style>
  :root {
    --ink-black: #0b0907;
    --smoke: #1a1511;
    --ember: #2a211a;
    --gold: #d4a500;
    --white: #ffffff;
  }
  * { margin: 0; padding: 0; box-sizing: border-box; }
  html, body {
    width: 1200px;
    height: 625px;
    overflow: hidden;
    background: var(--ink-black);
  }
  .hero {
    position: relative;
    width: 1200px;
    height: 625px;
    overflow: hidden;
  }
  .hero-backdrop {
    position: absolute;
    inset: 0;
    background:
      radial-gradient(ellipse 60% 55% at 55% 40%, var(--ember) 0%, transparent 70%),
      radial-gradient(ellipse 50% 50% at 20% 80%, #241c16 0%, transparent 70%),
      linear-gradient(160deg, var(--smoke) 0%, var(--ink-black) 100%);
  }
  .menu-toggle {
    position: absolute;
    top: 27px;
    left: 1016px;
    width: 22px;
    height: 18px;
    display: flex;
    flex-direction: column;
    justify-content: space-between;
    background: none;
    border: 0;
  }
  .menu-toggle span {
    display: block;
    height: 3px;
    border-radius: 2px;
    background: var(--white);
  }
  .hero-title {
    position: absolute;
    left: 0;
    right: 0;
    top: 186px;
    text-align: center;
    font-family: "Cinzel", serif;
    font-weight: 500;
    font-size: 126px;
    line-height: 112px;
    letter-spacing: 2px;
    color: transparent;
    -webkit-text-stroke: 1.4px var(--gold);
  }
  .hero-title .line { display: block; }
  .studio-mark {
    position: absolute;
    left: 495px;
    top: 207px;
    width: 210px;
    height: 210px;
    border-radius: 50%;
    border: 2px solid var(--gold);
    background: var(--ink-black);
    display: flex;
    align-items: center;
    justify-content: center;
    text-align: center;
  }
  .studio-mark .studio-name {
    font-family: "Cinzel", serif;
    font-weight: 700;
    font-size: 22px;
    line-height: 30px;
    letter-spacing: 3px;
    color: var(--gold);
  }
</style>
</head>
<body>
  <main class="hero">
    <div class="hero-backdrop" role="img" aria-label="Dimmed close-up photograph of a tattoo artist working with a tattoo machine on a client's arm"></div>

    <button class="menu-toggle" aria-label="Open menu">
      <span></span><span></span><span></span>
    </button>

    <h1 class="hero-title">
      <span class="line">The Gilded</span>
      <span class="line">Viper</span>
    </h1>

    <div class="studio-mark">
      <p class="studio-name">THE<br>GILDED<br>VIPER</p>
    </div>
  </main>
</body>
</html>
```